8" x 11" One Page Flyer for Fence Installation Company

We are looking to promote our business with a new flyer that would be handed out in person to people or put at their mailbox/door at their homes. The flyer needs to be creative and attention-grabbing. I have attached some of our previous flyers and our website information. Do not call or email regarding the flyer. We want the flyer to look professional but also friendly. One page, NOT folded. You can use images from our website at www.MyBraxtonYard.com or our Facebook page at www.Facebook.com/HollowbrookRailsBKT. We are flexible with what photos you can use but there must be photos of OUR fences on the flyer. More photos specifically can also be provided. Colors need to be suitable for a flyer printed on canary yellow in color paper OR white paper.

Target Market(s)

Homeowners that need a new fence

Industry/Entity Type

Construction

Font styles to use
Sans Serif
Other font styles liked:
• HD Colton

Colors
0054AA
0677BA
7BADD7
CADEEF
E8F1F8
0094D4
00A9DD
6FCCEA
C7EBF8
E9F6FB

Requirements
Must have
• Our fence photos - mostly wood fence photos (different designs), SIZE SHOULD BE LETTER SIZE 8" x 11"
Nice to have
• A nice bible verse featured at the bottom of the flyer.
Should not have
• DO NOT COPY THE WEBSITE FORMAT, I WANT SOMETHING UNIQUE. Other people's fence photos, they must all come from our website or facebook page

```html
<!DOCTYPE html>
<html lang="en">
<head>
<meta charset="utf-8">
<title>Hollowbrook Rails – Fence Flyer</title>
<link href="https://fonts.googleapis.com/css2?family=Montserrat:wght@400;500;600;700;800&display=swap" rel="stylesheet">
<style>
  :root {
    --bg: #e9e9e9;
    --brown-dark: #3b2212;
    --brown: #5a351c;
    --brown-mid: #744622;
    --orange: #f7941d;
    --orange-light: #fbb45c;
    --cream: #f6f3ee;
    --ink: #2d1c10;
    --white: #ffffff;
    --photo-grass: #6f8a3c;
    --photo-sky: #c9d3c4;
    --wood: #c9a46b;
  }
  * { box-sizing: border-box; margin: 0; padding: 0; }
  html, body { width: 900px; height: 1200px; overflow: hidden; }
  body { background: var(--bg); font-family: "Montserrat", sans-serif; position: relative; }

  .flyer {
    position: absolute; left: 37px; top: 12px; width: 826px; height: 1176px;
    background: var(--white); overflow: hidden;
    box-shadow: 0 4px 14px rgba(0,0,0,.18);
  }
  .sidebar {
    position: absolute; left: 0; top: 0; width: 312px; height: 100%;
    background: linear-gradient(90deg, var(--brown-dark) 0%, var(--brown) 45%, var(--brown-mid) 100%);
  }
  .header-bg {
    position: absolute; left: 312px; top: 0; right: 0; height: 225px;
    background: linear-gradient(180deg, var(--cream) 0%, var(--white) 100%);
  }

  .brand { position: absolute; left: 30px; top: 78px; display: flex; align-items: center; gap: 14px; color: var(--white); }
  .brand-mark { width: 46px; height: 46px; background: var(--white); }
  .brand-name { font-weight: 700; font-size: 22px; line-height: 1.1; }
  .brand-phone { font-weight: 700; font-size: 22px; line-height: 1.15; }
  .brand-tagline { font-size: 8px; font-weight: 600; margin-top: 3px; opacity: .9; }

  .headline { position: absolute; left: 337px; top: 40px; }
  .headline-top { font-weight: 800; font-size: 42px; letter-spacing: 7px; color: var(--brown-dark); line-height: 1; }
  .headline-main { font-weight: 700; font-size: 74px; color: var(--orange); line-height: 1; letter-spacing: 1px; margin-top: 4px; }
  .headline-sub { font-weight: 700; font-size: 18px; color: var(--brown); margin-top: 10px; }

  .hero-photo {
    position: absolute; left: 37px; top: 228px; width: 752px; height: 404px;
    border: 6px solid var(--white);
    background: linear-gradient(180deg, var(--photo-sky) 0%, #b9bfae 30%, var(--photo-grass) 50%, #5c7a2e 100%);
    box-shadow: 0 2px 6px rgba(0,0,0,.25);
  }

  .why { position: absolute; left: 30px; top: 668px; width: 270px; color: var(--white); }
  .why-title { font-weight: 800; font-size: 24px; }
  .why-title span { color: var(--orange); }
  .why-list { list-style: none; margin-top: 18px; }
  .why-list li { font-size: 13px; font-weight: 500; line-height: 26px; padding-left: 26px; position: relative; }
  .why-list li::before { content: ""; position: absolute; left: 2px; top: 9px; width: 8px; height: 8px; border-radius: 50%; background: var(--orange); }

  .showroom { position: absolute; left: 0; width: 312px; top: 938px; text-align: center; color: var(--white); font-weight: 700; font-size: 17px; line-height: 1.25; }
  .showroom span { color: var(--orange); display: block; font-size: 20px; }

  .showroom-pill {
    position: absolute; left: 25px; top: 1000px; width: 275px; height: 86px;
    background: linear-gradient(180deg, var(--orange-light), var(--orange));
    border-radius: 43px; border: 3px solid var(--white);
    display: flex; align-items: center; justify-content: center; text-align: center;
    font-weight: 700; font-size: 13.5px; line-height: 1.3; color: var(--brown-dark); padding: 0 14px;
  }

  .contact { position: absolute; left: 26px; top: 1118px; width: 282px; color: var(--white); font-size: 10.5px; font-weight: 600; line-height: 1.7; white-space: nowrap; }
  .contact .accent { color: var(--orange); }

  .gallery { position: absolute; left: 337px; top: 662px; width: 440px; height: 280px; display: grid; grid-template-columns: repeat(3, 1fr); grid-template-rows: repeat(2, 1fr); gap: 5px; }
  .gallery-photo { background: linear-gradient(160deg, var(--photo-grass), var(--wood)); }
  .gallery-photo.wood { background: linear-gradient(180deg, #d8b87d, var(--wood)); }
  .gallery-photo.side { background: linear-gradient(180deg, #9aa0a6, var(--wood)); }

  .about-tab { position: absolute; left: 337px; top: 954px; width: 200px; height: 34px; background: var(--orange); clip-path: polygon(0 0, 88% 0, 100% 100%, 0 100%); color: var(--white); font-weight: 800; font-size: 22px; padding: 3px 0 0 12px; }
  .about-tab span { color: var(--brown-dark); }
  .about-rule { position: absolute; left: 337px; top: 986px; width: 480px; height: 3px; background: var(--orange); }
  .about-text { position: absolute; left: 337px; top: 998px; width: 478px; font-size: 12.5px; line-height: 1.45; color: var(--ink); text-align: justify; }

  .web-band { position: absolute; left: 312px; right: 0; top: 1126px; height: 24px; background: var(--orange); color: var(--white); font-weight: 700; font-size: 13px; text-align: center; line-height: 24px; letter-spacing: .5px; }
  .web-band-under { position: absolute; left: 312px; right: 0; top: 1150px; height: 8px; background: var(--orange-light); opacity: .6; }
</style>
</head>
<body>
  <div class="flyer">
    <div class="sidebar"></div>
    <div class="header-bg"></div>

    <div class="brand">
      <div class="brand-mark"></div>
      <div>
        <div class="brand-name">Hollowbrook Rails</div>
        <div class="brand-phone">555-013-4471</div>
        <div class="brand-tagline">"Because Good Fences Make Good Neighbors"</div>
      </div>
    </div>

    <div class="headline">
      <div class="headline-top">WE BUILD</div>
      <div class="headline-main">FENCES....</div>
      <div class="headline-sub">And we would love to build your fence too!</div>
    </div>

    <div class="hero-photo" role="img" aria-label="Black aluminum fence with gate installed around a grassy backyard, houses behind"></div>

    <div class="why">
      <div class="why-title">WHY <span>CHOOSE</span> US?</div>
      <ul class="why-list">
        <li>Free Estimates</li>
        <li>Professional Installation</li>
        <li>Concrete in EVERY Post</li>
        <li>HOA Submission Assistance</li>
        <li>Lifetime Workmanship Warranty</li>
        <li>Experienced Installation Teams</li>
        <li>Quality Workmanship &amp; Materials</li>
        <li>FREE Gate Adjustments for LIFE</li>
      </ul>
    </div>

    <div class="showroom">VISIT OUR INDOOR &amp; OUTDOOR <span>SHOWROOM!</span></div>
    <div class="showroom-pill">Our outdoor showroom is open 24/7, while our indoor showroom and office is open</div>

    <div class="contact">
      <div>Monday - Thurs <span class="accent">9AM - 3PM</span>, Friday <span class="accent">9AM - 1PM</span></div>
      <div>MAIL US - office@mybraxtonyard.co</div>
    </div>

    <div class="gallery">
      <div class="gallery-photo" role="img" aria-label="Split rail wood fence along a yard"></div>
      <div class="gallery-photo" role="img" aria-label="Wood rail fence with trees behind"></div>
      <div class="gallery-photo side" role="img" aria-label="Wood fence beside a house"></div>
      <div class="gallery-photo side" role="img" aria-label="Narrow side yard with wood fence"></div>
      <div class="gallery-photo wood" role="img" aria-label="Close view of a wooden privacy fence"></div>
      <div class="gallery-photo wood" role="img" aria-label="Wood picket fence with pointed tops"></div>
    </div>

    <div class="about-tab">ABOUT <span>US?</span></div>
    <div class="about-rule"></div>
    <p class="about-text">Hollowbrook Rails consists of a growing team of individuals with over 30 years of experience within the fencing industry. Each member of our staff is well-trained and knowledgeable within their own specialty. All of our installers take pride in the work completed. In our eyes, we are only as successful as the completion of your job – each job is important to us and we strive to give you the best installation experience possible.</p>

    <div class="web-band">www.MyBraxtonYard.com</div>
    <div class="web-band-under"></div>
  </div>
</body>
</html>
```